KLVT, Inc.
Continental Meridian Holdings Group
Creative Brief
Corporate
H. Daniel Morrow, Ph.D.
Chief Executive Office
4172 South Birch Meadow Lane, Suite 300 Memphis, TN 38125
dr.danielmorrow@fernmail.example

```html
<!DOCTYPE html>
<html lang="en">
<head>
<meta charset="utf-8">
<title>KLVT, Inc. — Stationery Concept</title>
<link href="https://fonts.googleapis.com/css2?family=Open+Sans:wght@400;700&family=Libre+Baskerville&display=swap" rel="stylesheet">
<style>
  :root {
    --board: #8c8c8c;
    --board-light: #a3a3a3;
    --brand-blue: #233f9b;
    --brand-green: #1e9c78;
    --paper: #ffffff;
    --ink: #3a3a3a;
    --faint: #dfe4ef;
    --caption: #222222;
  }
  * { box-sizing: border-box; margin: 0; padding: 0; }
  html, body { width: 1200px; height: 427px; overflow: hidden; }
  body {
    background: radial-gradient(ellipse at 50% 45%, var(--board-light), var(--board));
    font-family: "Open Sans", Arial, sans-serif;
    position: relative;
  }
  .piece { position: absolute; }
  .caption {
    position: absolute;
    font-size: 6px;
    color: var(--caption);
    text-align: center;
    width: 100%;
  }
  .wordmark {
    display: flex; align-items: center; gap: 4px;
    color: var(--brand-blue); font-weight: 700; line-height: 1;
  }
  .wordmark .dot { border-radius: 50%; background: var(--brand-blue); flex: none; }
  .tagline { color: var(--brand-blue); font-weight: 400; }

  .brand-block { left: 24px; top: 92px; width: 150px; }
  .brand-block .wordmark { font-size: 26px; }
  .brand-block .dot { width: 18px; height: 18px; }
  .brand-block .tagline { font-size: 5px; margin-top: 3px; }
  .concept-title {
    font-family: "Libre Baskerville", Georgia, serif;
    font-size: 11px; color: var(--caption); margin-top: 16px;
  }

  .business-card { left: 24px; top: 170px; width: 80px; height: 66px; }
  .business-card .face { position: absolute; inset: 0; background: var(--paper); box-shadow: 0 1px 3px rgba(0,0,0,.35); overflow: hidden; }
  .business-card .wordmark { position: absolute; left: 6px; top: 14px; font-size: 13px; }
  .business-card .dot { width: 9px; height: 9px; }
  .business-card .holder { position: absolute; left: 6px; top: 38px; width: 38px; font-size: 3.4px; color: var(--ink); line-height: 1.45; }
  .business-card .lines { position: absolute; left: 46px; top: 37px; width: 32px; font-size: 3.2px; color: var(--ink); line-height: 1.5; white-space: nowrap; }
  .business-card .caption { top: 72px; }

  .letterhead { top: 24px; width: 278px; height: 360px; }
  .letterhead .sheet { position: absolute; inset: 0; background: var(--paper); box-shadow: 0 1px 4px rgba(0,0,0,.35); overflow: hidden; }
  .letterhead svg { position: absolute; inset: 0; }
  .letterhead .wordmark { position: absolute; left: 14px; top: 32px; font-size: 17px; }
  .letterhead .dot { width: 12px; height: 12px; }
  .letterhead .head-contact { position: absolute; right: 10px; top: 5px; font-size: 4px; color: var(--paper); line-height: 1.45; width: 82px; white-space: nowrap; }
  .letterhead .foot-contact { position: absolute; left: 0; right: 0; font-size: 3.6px; line-height: 1; color: var(--ink); text-align: center; white-space: nowrap; }
  .lh-a .foot-contact { bottom: 28px; }
  .lh-b .foot-contact { bottom: 15px; }
  .letterhead .caption { top: 370px; }
  .lh-a { left: 214px; }
  .lh-b { left: 509px; }

  .envelope { left: 816px; width: 360px; height: 126px; }
  .envelope svg { position: absolute; inset: 0; filter: drop-shadow(0 1px 2px rgba(0,0,0,.35)); }
  .env-green { top: 19px; }
  .env-blue { top: 101px; }
  .env-white { top: 180px; }
  .env-front { top: 242px; height: 142px; }
  .env-front .wordmark { position: absolute; left: 16px; top: 26px; font-size: 16px; }
  .env-front .dot { width: 11px; height: 11px; }
  .env-front .return { position: absolute; left: 16px; top: 50px; font-size: 4px; color: var(--ink); line-height: 1.4; }
  .env-front .caption { top: 150px; }
</style>
</head>
<body>

  <section class="piece brand-block">
    <div class="wordmark"><span class="dot"></span>KLVT</div>
    <div class="tagline">Continental Meridian Holdings Group</div>
    <h1 class="concept-title">Stationery Concept</h1>
  </section>

  <section class="piece business-card">
    <div class="face">
      <svg width="80" height="66" viewBox="0 0 80 66">
        <path d="M0 0H80V6Q40 12 0 4Z" fill="var(--brand-blue)"/>
        <path d="M0 60Q40 54 80 62V66H0Z" fill="var(--brand-green)"/>
      </svg>
      <div class="wordmark"><span class="dot"></span>KLVT</div>
      <div class="holder">H. Daniel Morrow, Ph.D.<br>Chief Executive Office</div>
      <div class="lines">P 901.555.0142<br>F 901.555.0143<br>dr.danielmorrow@<br>fernmail.example</div>
    </div>
    <p class="caption">Business Card</p>
  </section>

  <section class="piece letterhead lh-a">
    <div class="sheet">
      <svg width="278" height="360" viewBox="0 0 278 360">
        <path d="M0 0H278V26Q150 16 0 30Z" fill="var(--brand-blue)"/>
        <path d="M0 30Q150 16 278 26V29Q150 20 0 33Z" fill="var(--brand-green)"/>
        <circle cx="139" cy="185" r="70" fill="var(--faint)" opacity=".7"/>
        <path d="M0 344Q140 334 278 348V360H0Z" fill="var(--brand-green)" opacity=".85"/>
        <path d="M0 350Q140 342 278 353V360H0Z" fill="var(--brand-blue)"/>
      </svg>
      <div class="wordmark"><span class="dot"></span>KLVT</div>
      <div class="head-contact">P 901.555.0142<br>F 901.555.0143<br>dr.danielmorrow@fernmail.example</div>
      <div class="foot-contact">4172 South Birch Meadow Lane, Suite 300 Memphis, TN 38125</div>
    </div>
    <p class="caption">Letterhead Option A</p>
  </section>

  <section class="piece letterhead lh-b">
    <div class="sheet">
      <svg width="278" height="360" viewBox="0 0 278 360">
        <path d="M0 0H278V26Q150 16 0 30Z" fill="var(--brand-blue)"/>
        <path d="M0 30Q150 16 278 26V29Q150 20 0 33Z" fill="var(--brand-green)"/>
        <circle cx="139" cy="185" r="70" fill="var(--faint)" opacity=".7"/>
        <path d="M0 353Q140 347 278 355" stroke="var(--brand-blue)" stroke-width="1" fill="none"/>
      </svg>
      <div class="wordmark"><span class="dot"></span>KLVT</div>
      <div class="head-contact">P 901.555.0142<br>F 901.555.0143<br>dr.danielmorrow@fernmail.example</div>
      <div class="foot-contact">4172 South Birch Meadow Lane, Suite 300 Memphis, TN 38125 · dr.danielmorrow@fernmail.example</div>
    </div>
    <p class="caption">Letterhead Option B</p>
  </section>

  <section class="piece envelope env-green">
    <svg width="360" height="126" viewBox="0 0 360 126">
      <rect width="360" height="126" fill="#188e6c"/>
      <path d="M0 0L180 84L360 0Z" fill="var(--brand-green)"/>
      <circle cx="180" cy="70" r="6" fill="var(--paper)"/>
    </svg>
  </section>

  <section class="piece envelope env-blue">
    <svg width="360" height="126" viewBox="0 0 360 126">
      <rect width="360" height="126" fill="#1d3688"/>
      <path d="M0 0L180 84L360 0Z" fill="var(--brand-blue)"/>
      <circle cx="180" cy="70" r="6" fill="var(--paper)"/>
    </svg>
  </section>

  <section class="piece envelope env-white">
    <svg width="360" height="126" viewBox="0 0 360 126">
      <rect width="360" height="126" fill="#f1f1f1"/>
      <path d="M0 0L180 84L360 0Z" fill="var(--paper)" stroke="#d8d8d8" stroke-width=".6"/>
      <circle cx="180" cy="70" r="6" fill="var(--brand-blue)"/>
    </svg>
  </section>

  <section class="piece envelope env-front">
    <svg width="360" height="142" viewBox="0 0 360 142">
      <rect width="360" height="142" fill="var(--paper)"/>
      <path d="M0 0H360V12Q200 6 0 20Z" fill="var(--brand-blue)"/>
      <path d="M0 20Q200 6 360 12V15Q200 10 0 23Z" fill="var(--brand-green)"/>
      <path d="M0 132Q180 124 360 134V142H0Z" fill="var(--brand-blue)"/>
    </svg>
    <div class="wordmark"><span class="dot"></span>KLVT</div>
    <div class="return">4172 South Birch Meadow Lane, Suite 300<br>Memphis, TN 38125</div>
    <p class="caption">Envelope Front &amp; Back</p>
  </section>

</body>
</html>
```